Hunting Ethics Organization Needs a Web Design with Logo Refresh

This project involves the creation of a website design including the homepage design, inside page design, and logo refinements. Our organization is Talveth, and we are a not-for-profit hunting ethics organization.
The focus of the new website design is to bring attention the mission of our organization, provide an overview of the areas where our organization deploys its resources to support the modern hunter, and to encourage visitors to support our organization by donating in support of the organization’s mission.
The winning design will be implemented in Wordpress by our in-house team. If you have questions about how any particular design element may translate to Wordpress, please feel free to post questions in response to this brief. In general, however, we’re more focused on the evolution and delivery of a strong overall design aesthetic – we’ll shoulder the responsibility of how we translate that design into Wordpress.
See attached design brief for full details.
Hunting
2 page

```html
<!DOCTYPE html>
<html lang="en">
<head>
<meta charset="utf-8">
<title>Talveth – The Hunter's Institute</title>
<link href="https://fonts.googleapis.com/css2?family=Open+Sans:ital,wght@0,300;0,400;0,600;0,700;1,400&display=swap" rel="stylesheet">
<style>
:root{
  --blue:#2566a8;
  --blue-dark:#1d5995;
  --olive:#a79b5e;
  --ink:#333333;
  --grey:#7a7a7a;
  --light-grey:#9a9a9a;
  --nav:#1f1f1f;
  --white:#ffffff;
}
*{box-sizing:border-box;margin:0;padding:0}
html,body{width:1200px;height:2500px;overflow:hidden;background:var(--white)}
body{position:relative;font-family:'Open Sans',Arial,sans-serif;color:var(--ink)}
.abs{position:absolute}

/* header */
.site-header{position:absolute;left:0;top:0;width:1200px;height:84px;border-bottom:2px solid #e6e6e6}
.brand{position:absolute;left:100px;top:18px;display:flex;align-items:center;gap:12px}
.brand-mark{width:40px;height:40px;border-radius:50%;background:var(--blue)}
.brand-name{font-size:30px;font-weight:700;color:var(--blue);letter-spacing:1px}
.contact-item{position:absolute;top:25px;display:flex;align-items:center;gap:14px}
.contact-icon{width:37px;height:37px;border-radius:50%;background:var(--olive);display:flex;align-items:center;justify-content:center}
.contact-label{font-size:14px;color:var(--light-grey);line-height:17px}
.contact-value{font-size:18px;color:#4a5a6a;line-height:22px}
.donate-btn{position:absolute;left:993px;top:25px;width:107px;height:37px;background:var(--blue);color:var(--white);font-size:11px;font-weight:700;display:flex;align-items:center;justify-content:center;letter-spacing:.5px}

/* nav */
.main-nav{position:absolute;left:0;top:87px;width:1200px;height:45px;background:var(--nav)}
.main-nav a{position:absolute;top:0;line-height:45px;transform:translateX(-50%);color:var(--white);font-size:13px;font-weight:700;text-decoration:none;white-space:nowrap}

/* hero */
.hero{position:absolute;left:0;top:132px;width:1200px;height:493px;background:linear-gradient(90deg,#3b3a32 0%,#5d5a4c 35%,#6c6450 55%,#3e4433 80%,#2b3424 100%)}
.hero-title{position:absolute;left:100px;top:168px;font-size:43px;font-weight:700;line-height:46px;color:var(--white);letter-spacing:1px}
.hero-title span{display:block;color:var(--olive)}
.hero-lines{position:absolute;left:100px;top:262px;font-size:18px;font-weight:700;line-height:32px;color:var(--white)}
.btn-outline{position:absolute;border:2px solid var(--white);color:var(--white);display:flex;align-items:center;justify-content:center;font-weight:600}
.hero-arrow{position:absolute;top:226px;width:38px;height:38px;border-radius:50%;background:rgba(0,0,0,.3);display:flex;align-items:center;justify-content:center}

/* welcome */
.welcome{position:absolute;left:0;top:625px;width:1200px;height:303px;background:var(--blue)}
.welcome-title{position:absolute;right:667px;top:40px;text-align:right;color:var(--white);font-size:53px;line-height:60px;font-weight:300}
.welcome-title strong{display:block;font-weight:700}
.welcome-text{position:absolute;left:630px;top:45px;width:390px;font-size:13px;line-height:25px;color:var(--white)}

/* cards */
.card{position:absolute;top:827px;width:322px;height:195px;background:var(--white);box-shadow:0 4px 8px rgba(0,0,0,.18)}
.card-photo{position:absolute;left:13px;top:13px;width:296px;height:140px}
.card-label{position:absolute;left:13px;top:153px;width:296px;height:38px;background:var(--blue);color:var(--white);font-size:13px;font-weight:700;line-height:38px;padding-left:18px}
.card-body{position:absolute;top:1033px;width:296px}
.card-body h3{font-size:14px;font-weight:700;line-height:24px;color:#4a4a4a;margin-bottom:8px}
.card-body p{font-size:11.5px;line-height:22px;color:var(--grey)}

/* news */
.section-title{position:absolute;left:0;width:1200px;text-align:center;font-size:23px;font-weight:700;color:var(--ink)}
.section-sub{position:absolute;left:0;width:1200px;text-align:center;font-size:14px;color:var(--light-grey)}
.news-photo{position:absolute;top:1323px;width:165px;height:124px}
.news-text{position:absolute;top:1323px;width:285px}
.news-text h4{font-size:11.5px;line-height:20px;font-weight:700;color:var(--blue);text-transform:uppercase}
.news-text .date{font-size:11.5px;line-height:24px;color:var(--ink)}
.news-text p{font-size:11.5px;line-height:22px;color:var(--grey)}

/* about */
.about{position:absolute;left:0;top:1522px;width:1200px;height:398px;background:linear-gradient(180deg,#1c1f1a 0%,#2b2d25 55%,#3a3a30 100%)}
.about-title{position:absolute;left:0;top:80px;width:1200px;text-align:center;font-size:43px;font-weight:700;color:var(--olive)}
.about-title span{color:var(--blue)}
.about-sub{position:absolute;left:0;top:146px;width:1200px;text-align:center;font-size:16px;font-weight:700;color:var(--white)}
.about-text{position:absolute;left:200px;top:184px;width:800px;text-align:center;font-size:14px;line-height:30px;color:#e6e6e6}

/* testimonial */
.avatar{position:absolute;left:247px;top:2000px;width:120px;height:120px;border-radius:50%}
.quote{position:absolute;left:418px;top:2008px;width:540px;font-size:11.5px;line-height:23px;font-style:italic;color:var(--light-grey)}
.quote-mark{position:absolute;font-size:34px;color:#cfcfcf;font-family:Georgia,serif}
.author{position:absolute;left:418px;top:2100px}
.author-name{font-size:11.5px;font-weight:700;color:var(--blue);line-height:20px}
.author-role{font-size:11.5px;color:var(--grey);line-height:20px}

/* footer */
.site-footer{position:absolute;left:0;top:2200px;width:1200px;height:250px;background:var(--blue)}
.footer-brand{position:absolute;left:103px;top:92px;display:flex;align-items:center;gap:10px;color:#e9e2c4;font-size:36px;font-weight:400;letter-spacing:1px}
.footer-brand i{display:block;width:30px;height:30px;border-radius:50%;background:#e9e2c4}
.footer-col{position:absolute;top:40px;color:var(--white)}
.footer-col h5{font-size:12px;font-weight:700;margin-bottom:10px;letter-spacing:.3px}
.footer-col li{list-style:none;font-size:11px;line-height:22.3px}
.footer-row{display:flex;align-items:center;gap:10px}
.social li{display:flex;align-items:center;gap:12px;line-height:35px}
.social .sq{width:24px;height:24px;border:1px solid var(--white)}
.bottom-bar{position:absolute;left:0;top:2450px;width:1200px;height:50px;background:var(--blue-dark);color:var(--white);font-size:11px;text-align:center;line-height:50px}
</style>
</head>
<body>

<header class="site-header">
  <div class="brand"><span class="brand-mark"></span><span class="brand-name">Talveth</span></div>
  <div class="contact-item" style="left:583px">
    <div class="contact-icon"><svg width="16" height="16" viewBox="0 0 24 24"><path fill="#fff" d="M6.6 10.8a15 15 0 0 0 6.6 6.6l2.2-2.2c.3-.3.7-.4 1-.2 1.1.4 2.3.6 3.6.6.6 0 1 .4 1 1V20c0 .6-.4 1-1 1A17 17 0 0 1 3 4c0-.6.4-1 1-1h3.5c.6 0 1 .4 1 1 0 1.3.2 2.5.6 3.6.1.3 0 .7-.2 1z"/></svg></div>
    <div><div class="contact-label">Call Us :</div><div class="contact-value">( 3265 ) 410 882</div></div>
  </div>
  <div class="contact-item" style="left:783px">
    <div class="contact-icon"><svg width="16" height="16" viewBox="0 0 24 24"><path fill="#fff" d="M3 5h18v2l-9 6-9-6zM3 9l9 6 9-6v10H3z"/></svg></div>
    <div><div class="contact-label">Email Us :</div><div class="contact-value">info@talveth.org</div></div>
  </div>
  <a class="donate-btn">DONATE</a>
</header>

<nav class="main-nav">
  <a style="left:147px">HOME</a>
  <a style="left:287px">ABOUT US</a>
  <a style="left:458px">HUNTING ETHICS</a>
  <a style="left:645px">CONSERVATION</a>
  <a style="left:827px">GET INVOLVED</a>
  <a style="left:998px">CONTACT US</a>
</nav>

<section class="hero" role="img" aria-label="Photo of a hunter in a camouflage cap aiming a scoped rifle">
  <div class="hero-arrow" style="left:33px"><svg width="14" height="14" viewBox="0 0 14 14"><path d="M9 2 4 7l5 5" stroke="#fff" stroke-width="2" fill="none"/></svg></div>
  <div class="hero-arrow" style="left:1123px"><svg width="14" height="14" viewBox="0 0 14 14"><path d="m5 2 5 5-5 5" stroke="#fff" stroke-width="2" fill="none"/></svg></div>
</section>
<h1 class="hero-title" style="top:300px">THE HUNTER'S<span>INSTITUTE</span></h1>
<div class="hero-lines" style="top:392px">PROTECT THE HERITAGE OF HUNTING<br>HELP US PROTECT THE FUTURE OF HUNTING<br>SUPPORT US AS WE EMPOWER THE MODERN HUNTER</div>
<a class="btn-outline" style="left:100px;top:503px;width:164px;height:46px;font-size:14px">GET INVOLVED</a>

<section class="welcome">
  <h2 class="welcome-title">WELCOME TO<strong>TALVETH</strong></h2>
  <p class="welcome-text">Lorem Ipsum is simply dummy text of the printing and typesetting industry. Lorem Ipsum has been the industry's standard dummy text ever since the 1500s, when an unknown printer took a galley of type and scrambled it to make a type specimen...</p>
</section>

<article class="card" style="left:100px">
  <div class="card-photo" role="img" aria-label="Silhouette of a hunter aiming at sunset" style="background:linear-gradient(90deg,#2a1a08,#c8801e 60%,#3a2410)"></div>
  <div class="card-label">HUNTING ETHICS</div>
</article>
<article class="card" style="left:440px">
  <div class="card-photo" role="img" aria-label="Hunter carrying game birds in a field" style="background:linear-gradient(90deg,#6b6248,#8e8566 50%,#5b5440)"></div>
  <div class="card-label">CONSERVATION</div>
</article>
<article class="card" style="left:778px">
  <div class="card-photo" role="img" aria-label="Young hunter aiming a scoped rifle outdoors" style="background:linear-gradient(90deg,#5a3a22,#8a6a4a 50%,#4a4030)"></div>
  <div class="card-label">GET INVOLVED</div>
</article>

<div class="card-body" style="left:116px"><h3>Lorem Ipsum is simply dummy text of the printing and typesetting</h3><p>Lorem Ipsum is simply dummy text of the printing and typesetting industry. Lorem Ipsum has been the industry's standard dummy text ever...</p></div>
<div class="card-body" style="left:456px"><h3>Lorem Ipsum is simply dummy text of the printing and typesetting</h3><p>Lorem Ipsum is simply dummy text of the printing and typesetting industry. Lorem Ipsum has been the industry's standard dummy text ever...</p></div>
<div class="card-body" style="left:794px"><h3>Lorem Ipsum is simply dummy text of the printing and typesetting</h3><p>Lorem Ipsum is simply dummy text of the printing and typesetting industry. Lorem Ipsum has been the industry's standard dummy text ever...</p></div>

<h2 class="section-title" style="top:1216px">RECENT NEWS</h2>
<p class="section-sub" style="top:1262px">Lorem Ipsum is simply dummy text of the printing and typesetting industry. Lorem Ipsum has been the industry's...</p>

<div class="news-photo" style="left:98px;background:linear-gradient(180deg,#9fb4c4,#6c7660)" role="img" aria-label="Hunter in camouflage holding a rifle"></div>
<div class="news-text" style="left:293px"><h4>Lorem Ipsum is simply dummy text of the printing</h4><div class="date">Posted on 27 Febraury 2015</div><p>Lorem Ipsum is simply dummy text of the printing and typesetting industry. Lorem Ipsum has been the industry's standard dummy text ever...</p></div>
<div class="news-photo" style="left:622px;background:linear-gradient(90deg,#5a4a34,#b59a6a 60%,#6a5a40)" role="img" aria-label="Hunting dog sitting beside a hunter"></div>
<div class="news-text" style="left:817px"><h4>Lorem Ipsum is simply dummy text of the printing</h4><div class="date">Posted on 27 Febraury 2015</div><p>Lorem Ipsum is simply dummy text of the printing and typesetting industry. Lorem Ipsum has been the industry's standard dummy text ever...</p></div>

<section class="about" role="img" aria-label="Dark photo of a hunter resting a rifle on rocks">
  <h2 class="about-title">ABOUT <span>TALVETH</span></h2>
  <p class="about-sub">ES SIMPLEMENTE EL TEXTO DE RELLENO DE LAS IMPRENTAS Y ARCHIVOS DE TEXTO</p>
  <p class="about-text">It is a long established fact that a reader will be distracted by the readable content of a page when looking at its layout. The point of using Lorem Ipsum is that it has a more-or-less normal distribution of letters...</p>
  <a class="btn-outline" style="left:498px;top:268px;width:202px;height:45px;font-size:11px;font-weight:400">CLICK HERE FOR MORE INFO</a>
</section>

<div class="avatar" role="img" aria-label="Portrait of the quoted team member" style="background:radial-gradient(circle at 50% 40%,#8a6a50,#3a2a20)"></div>
<span class="quote-mark" style="left:392px;top:1990px">“</span>
<p class="quote">Lorem Ipsum is simply dummy text of the printing and typesetting industry. Lorem Ipsum has been the industry's standard dummy text ever since the 1500s, when an unknown printer took a galley of type and scrambled it to make a type specimen book...</p>
<span class="quote-mark" style="left:965px;top:2050px">”</span>
<div class="author"><div class="author-name">MARCUS HALE</div><div class="author-role">Marketing Executive</div></div>
<svg class="abs" style="left:955px;top:2122px" width="24" height="12" viewBox="0 0 24 12"><path d="M6 2 2 6l4 4M18 2l4 4-4 4" stroke="#999" stroke-width="1.4" fill="none"/></svg>

<footer class="site-footer">
  <div class="footer-brand"><i></i>TALVETH</div>
  <div class="footer-col" style="left:332px"><h5>WELCOME</h5><ul><li>Home</li><li>About Us</li><li>Hunting Ethics</li><li>Conservation</li><li>Get Involved</li><li>Contact Us</li><li>Donate</li></ul></div>
  <div class="footer-col" style="left:518px"><h5>INFORMATION</h5><ul><li>Terms &amp; Condition</li><li>Privacy Policy</li><li>Disclaimer</li><li>Sitemap</li></ul></div>
  <div class="footer-col" style="left:733px"><h5>CONTACT INFO</h5><ul>
    <li>120 Street name, City name,</li><li>Country name, Zpcode : 3652236</li>
    <li class="footer-row" style="margin-top:8px"><svg width="11" height="11" viewBox="0 0 24 24"><path fill="#fff" d="M6.6 10.8a15 15 0 0 0 6.6 6.6l2.2-2.2c.3-.3.7-.4 1-.2 1.1.4 2.3.6 3.6.6.6 0 1 .4 1 1V20c0 .6-.4 1-1 1A17 17 0 0 1 3 4c0-.6.4-1 1-1h3.5c.6 0 1 .4 1 1 0 1.3.2 2.5.6 3.6.1.3 0 .7-.2 1z"/></svg>( 3652 ) 718 204</li>
    <li class="footer-row" style="margin-top:4px"><svg width="11" height="11" viewBox="0 0 24 24"><path fill="#fff" d="M3 5h18v2l-9 6-9-6zM3 9l9 6 9-6v10H3z"/></svg>info@talveth.org</li>
  </ul></div>
  <div class="footer-col social" style="left:968px"><h5>FOLLOW US</h5><ul>
    <li><span class="sq"></span>: Campfire</li><li><span class="sq"></span>: Chirpline</li><li><span class="sq"></span>: Plusboard</li><li><span class="sq"></span>: Linkwork</li>
  </ul></div>
</footer>
<div class="bottom-bar">© Copyrights. 2015. Talveth. All rights reserved.</div>

</body>
</html>
```